Business Card Design for my Real Estate Investing Company

This is for a Real Estate Investing Company that will be serving the Las Vegas Valley. Id like the following slogan included: "Investing in Our Community" I have attached my logo. You will see the color tones I'm interested in..in my logo. I would like the card to be double-sided with a modern, professional look.
Target Market(s)
Homeowners, banks, real estate industry
Industry/Entity Type
Real Estate
Contact Information for Business Card
name: Dale Pruitt
position: Managing Member
address: 4812 Corvane Pkwy ste 207-300
N. Las Vegas, NV 89517
phone: (702) 555-0143
fax: (702) 555-0187
email: OakridgeHousePurchaser@examplemail.com
web: OakridgeHousePurchasers.example
*At the bottom of the card I would like....
We buy houses for cash....no repairs, no commissions, no fees!
Logo Text
OAKRIDGE HOUSE PURCHASERS "Investing in Our Community"
Font styles to use
Other font styles liked:
- Lora
Requirements
Must have
- On the back of the card, i'd like to have my logo large and the following statements:
- Are you considering selling your home? Want a simple, hassle-free transaction? We can help! We buy houses for cash and can close quickly! No need to do any repairs, no realtor commissions, no closing costs.....and no headaches. Let us help you with your real estate needs...!
Nice to have
- multiple colors 2 two tone on front and back

```html
<!DOCTYPE html>
<html lang="en">
<head>
<meta charset="utf-8">
<title>Oakridge House Purchasers – Business Card</title>
<link rel="stylesheet" href="https://fonts.googleapis.com/css2?family=Lora:wght@400;700&family=Roboto:wght@400;500&display=swap">
<style>
  :root {
    --page-bg: #e6e6e6;
    --card-black: #0b0b0d;
    --card-black-soft: #1c1c20;
    --brand-blue: #1d5fb3;
    --brand-blue-light: #2f78cf;
    --text-white: #ffffff;
    --text-muted: #c9ccd2;
    --rule: #5a5d63;
  }
  * { margin: 0; padding: 0; box-sizing: border-box; }
  html, body {
    width: 1200px; height: 841px; overflow: hidden;
    background: var(--page-bg);
  }
  .canvas {
    width: 1200px; height: 841px;
    display: flex; align-items: center; justify-content: center; gap: 40px;
  }
  .card {
    position: relative;
    width: 540px; height: 309px;
    background: linear-gradient(135deg, var(--card-black-soft) 0%, var(--card-black) 55%);
    color: var(--text-white);
    overflow: hidden;
    border-radius: 4px;
    box-shadow: 0 6px 18px rgba(0,0,0,0.25);
  }
  .card-wave { position: absolute; inset: 0; width: 540px; height: 309px; }

  /* Front */
  .holder { position: absolute; left: 40px; top: 22px; }
  .holder-name {
    font-family: "Lora", serif; font-weight: 700; font-size: 30px; line-height: 1.1;
  }
  .holder-title {
    font-family: "Lora", serif; font-size: 14px; letter-spacing: 0.5px; margin-top: 2px;
  }
  .contact {
    position: absolute; left: 18px; top: 150px;
    font-family: "Roboto", sans-serif; font-size: 11.5px; color: var(--text-white);
    list-style: none;
  }
  .contact-address { margin-left: 0; line-height: 1.4; padding-bottom: 5px;
    border-bottom: 1px solid var(--rule); margin-bottom: 5px; width: 190px; }
  .contact-item { display: flex; align-items: center; gap: 7px; line-height: 1.75; }
  .contact-icon { width: 11px; height: 11px; flex: none; }
  .tagline {
    position: absolute; left: 40px; bottom: 14px;
    font-family: "Roboto", sans-serif; font-size: 12.5px; color: var(--text-white);
  }
  .brand { position: absolute; text-align: center; }
  .brand-front { right: 26px; top: 180px; width: 250px; }
  .brand-line { display: flex; align-items: center; justify-content: center; gap: 8px; }
  .brand-mark { width: 12px; height: 12px; background: var(--brand-blue-light); flex: none; }
  .brand-name {
    font-family: "Lora", serif; font-weight: 700; color: var(--brand-blue-light);
    font-size: 17px; letter-spacing: 0.5px;
  }
  .brand-slogan {
    font-family: "Lora", serif; font-size: 10.5px; letter-spacing: 1.5px;
    color: var(--text-white); margin-top: 4px;
  }

  /* Back */
  .brand-back { left: 0; right: 0; top: 62px; }
  .brand-back .brand-mark { width: 18px; height: 18px; }
  .brand-back .brand-name { font-size: 26px; }
  .brand-back .brand-slogan { font-size: 13px; margin-top: 6px; }
  .divider { position: absolute; left: 80px; top: 150px; width: 380px; height: 8px; }
  .pitch {
    position: absolute; left: 40px; right: 40px; top: 170px;
    font-family: "Lora", serif; font-size: 11.5px; line-height: 1.55; text-align: center;
    color: var(--text-white);
  }
</style>
</head>
<body>
<main class="canvas">

  <section class="card card-front" aria-label="Card front">
    <svg class="card-wave" viewBox="0 0 540 309" aria-hidden="true">
      <path d="M0 0 H540 V205 C525 150 470 115 390 118 C320 122 270 140 200 135 C110 128 40 100 0 85 Z" fill="var(--brand-blue)"/>
      <path d="M0 92 C40 108 110 136 200 142 C270 147 320 130 390 126" fill="none" stroke="#fff" stroke-width="4"/>
      <path d="M360 128 C450 118 515 160 530 215" fill="none" stroke="#fff" stroke-width="5"/>
    </svg>

    <div class="holder">
      <h1 class="holder-name">Dale Pruitt</h1>
      <p class="holder-title">MANAGING MEMBER</p>
    </div>

    <ul class="contact">
      <li class="contact-address">4812 Corvane Pkwy ste 207-300<br>N. Las Vegas, NV 89517</li>
      <li class="contact-item">
        <svg class="contact-icon" viewBox="0 0 12 12"><circle cx="6" cy="6" r="5.5" fill="none" stroke="#9aa" stroke-width="1"/><path d="M4 3.5 L5 3.5 L5.6 5 L5 5.6 C5.4 6.4 5.8 6.8 6.6 7.2 L7.2 6.6 L8.5 7.2 L8.5 8.2 C6 8.4 3.8 6 4 3.5Z" fill="#cdd"/></svg>
        (702) 555-0143</li>
      <li class="contact-item">
        <svg class="contact-icon" viewBox="0 0 12 12"><circle cx="6" cy="6" r="5.5" fill="none" stroke="#9aa" stroke-width="1"/><rect x="3.5" y="4.5" width="5" height="3.5" fill="#cdd"/><rect x="4.3" y="3" width="3.4" height="1.5" fill="#cdd"/></svg>
        (702) 555-0187</li>
      <li class="contact-item">
        <svg class="contact-icon" viewBox="0 0 12 12"><circle cx="6" cy="6" r="5.5" fill="none" stroke="#9aa" stroke-width="1"/><rect x="3" y="4" width="6" height="4" fill="none" stroke="#cdd" stroke-width="0.9"/><path d="M3 4 L6 6.3 L9 4" fill="none" stroke="#cdd" stroke-width="0.9"/></svg>
        OakridgeHousePurchaser@examplemail.com</li>
      <li class="contact-item">
        <svg class="contact-icon" viewBox="0 0 12 12"><circle cx="6" cy="6" r="5.5" fill="none" stroke="#9aa" stroke-width="1"/><path d="M3.5 6 H8.5 M6.5 4 L8.5 6 L6.5 8" fill="none" stroke="#cdd" stroke-width="1"/></svg>
        OakridgeHousePurchasers.example</li>
    </ul>

    <div class="brand brand-front">
      <div class="brand-line">
        <span class="brand-mark"></span>
        <span class="brand-name">OAKRIDGE HOUSE PURCHASERS</span>
      </div>
      <p class="brand-slogan">"Investing in Our Community"</p>
    </div>

    <p class="tagline">We buy houses for cash....no repairs, no commissions, no fees!</p>
  </section>

  <section class="card card-back" aria-label="Card back">
    <div class="brand brand-back">
      <div class="brand-line">
        <span class="brand-mark"></span>
        <span class="brand-name">OAKRIDGE HOUSE PURCHASERS</span>
      </div>
      <p class="brand-slogan">"Investing in Our Community"</p>
    </div>

    <svg class="divider" viewBox="0 0 380 8" aria-hidden="true">
      <line x1="4" y1="4" x2="376" y2="4" stroke="#fff" stroke-width="1.2"/>
      <circle cx="4" cy="4" r="3" fill="#fff"/>
      <circle cx="376" cy="4" r="3" fill="#fff"/>
    </svg>

    <p class="pitch">
      Are you considering selling your home? Want a simple, hassle-free transaction? We can help!<br>
      We buy houses for cash and can close quickly!<br>
      No need to do any repairs, no realtor commissions, no closing costs.....and no headaches.<br>
      Let us help you with your real estate needs...!
    </p>
  </section>

</main>
</body>
</html>
```